Occupational Therapy Clinic Advertisement

Create an advertisement for a magazine. Below I have attached my original ad (Ad 2020.pdf) . I want the ad changed and it should be eye catching. I would like a eye catching graphics added in the ad. It should be a graphic image that applies to education. I am attaching a sample graphic image of that I liked from someone elses ad- it should not be the same- it just is there to show what I like. Please use the same words from my original ad.Dimensions: 3.75in x 10.3 in

Target Market(s)

Parents of School aged children

Requirements
Must have
• Must have eye catching Graphic. Colors should be eye catching for a typed magazine.

```html
<!DOCTYPE html>
<html lang="en">
<head>
<meta charset="utf-8">
<title>Bright Path OT Services – Magazine Ad</title>
<link href="https://fonts.googleapis.com/css2?family=Bebas+Neue&family=Lato:wght@400;700&display=swap" rel="stylesheet">
<style>
  :root{
    --page-bg:#b0c4de;
    --paper:#f4f4f4;
    --brand-blue:#2a5ea6;
    --ink:#333333;
    --ink-soft:#555555;
    --orange-top:#ffc43a;
    --orange-bottom:#f79200;
    --row-light:#e3e7ee;
    --pink-light:#f78fae;
    --pink:#f7296a;
    --white:#ffffff;
    --art-mint:#cfe9dc;
    --art-cream:#f6f1de;
  }
  *{box-sizing:border-box;margin:0;padding:0}
  html,body{width:1200px;height:1200px;overflow:hidden}
  body{background:var(--page-bg);font-family:"Lato",sans-serif;position:relative}
  .ad{position:absolute;left:410px;top:78px;width:380px;height:1044px;
      background:linear-gradient(160deg,#ececec,var(--paper) 40%,#f9f9f9);overflow:hidden}
  .brand-name{position:absolute;top:30px;left:0;width:100%;text-align:center;
      font-family:"Bebas Neue",sans-serif;font-size:64px;line-height:1;color:var(--brand-blue);letter-spacing:1px}
  .brand-tagline{position:absolute;top:94px;width:100%;text-align:center;font-size:21px;color:var(--ink)}
  .pill{position:absolute;border-radius:8px;
      background:linear-gradient(var(--orange-top),var(--orange-bottom));
      box-shadow:0 1px 2px rgba(0,0,0,.2);text-align:center;color:#3a2500}
  .phone-pill{left:120px;top:129px;width:139px;height:25px;font-size:16px;line-height:25px}
  .question{position:absolute;font-family:"Bebas Neue",sans-serif;font-size:23px;line-height:24px;color:var(--ink)}
  .question--left{right:219px;top:178px;text-align:right}
  .question--right{left:210px;top:175px}
  .question--wide{left:0;width:100%;top:280px;text-align:center}
  .divider-v{position:absolute;left:185px;top:167px;height:96px;border-left:2px dotted var(--ink-soft)}
  .divider-h{position:absolute;left:29px;width:321px;border-top:2px dotted var(--ink-soft)}
  .success-pill{left:38px;top:356px;width:303px;height:31px;font-family:"Bebas Neue",sans-serif;
      font-size:21px;line-height:32px;color:#2a1a00}
  .service-row{position:absolute;left:25px;width:325px;height:27px;display:flex;gap:4px}
  .service-row__label{width:97px;background:var(--brand-blue);color:var(--white);
      font-family:"Bebas Neue",sans-serif;font-size:20px;line-height:28px;padding-left:5px}
  .service-row__text{flex:1;background:var(--row-light);color:var(--ink-soft);font-size:13px;line-height:27px;padding-left:14px}
  .education-art{position:absolute;left:24px;top:510px;width:328px;height:217px;border-radius:12px;
      background:radial-gradient(ellipse at 50% 35%,var(--art-mint),var(--art-cream) 70%,transparent 100%)}
  .footer-band{position:absolute;left:0;top:806px;width:100%;height:238px;
      background:linear-gradient(var(--pink-light),var(--pink) 45%);border-top:2px solid var(--pink)}
  .promise-pill{position:absolute;left:136px;top:782px;width:190px;height:45px;border-radius:0 23px 23px 0;
      background:var(--brand-blue);color:var(--white);font-size:13px;line-height:16px;padding:7px 0 0 30px}
  .age-badge{position:absolute;left:58px;top:761px;width:90px;height:90px;border-radius:50%;
      background:radial-gradient(var(--orange-top),var(--orange-bottom));text-align:center;
      font-family:"Bebas Neue",sans-serif;color:#231500}
  .age-badge::before{content:"";position:absolute;inset:5px;border-radius:50%;border:1.5px dotted #3a2500}
  .age-badge__label{display:block;font-size:24px;line-height:24px;padding-top:14px}
  .age-badge__range{display:block;font-size:36px;line-height:32px}
  .footer-info{position:absolute;top:870px;width:100%;text-align:center;color:var(--white);font-size:13px;line-height:15.3px}
  .footer-rule{position:absolute;left:147px;top:960px;width:84px;border-top:1.5px solid var(--white)}
  .contact{position:absolute;top:970px;width:100%;text-align:center;color:var(--white);font-weight:700;font-size:17px;line-height:21px}
</style>
</head>
<body>
  <article class="ad">
    <h1 class="brand-name">Bright Path</h1>
    <p class="brand-tagline">OT SERVICES</p>
    <p class="pill phone-pill">(555) 014-2276</p>

    <p class="question question--left">Does your child<br>struggle with<br>reading/kriah?</p>
    <div class="divider-v"></div>
    <p class="question question--right">Knows the<br>information but<br>fails the test?</p>

    <div class="divider-h" style="top:271px"></div>
    <p class="question question--wide">Has difficulty remembering<br>names and dates?</p>
    <div class="divider-h" style="top:338px"></div>

    <p class="pill success-pill">Yes your child can will succeed in school!</p>

    <div class="service-row" style="top:410px">
      <span class="service-row__label">We Evaluate</span>
      <span class="service-row__text">Using standardized Evaluations</span>
    </div>
    <div class="service-row" style="top:441px">
      <span class="service-row__label">We Treat:</span>
      <span class="service-row__text">Using Researched based techniques</span>
    </div>

    <div class="education-art" role="img" aria-label="Illustration of an open book with school icons — pencil, atom, crayon, globe, flask and book — rising from its pages in mint circles"></div>

    <div class="footer-band"></div>
    <p class="promise-pill">We Treat the underlying<br>processing deficits</p>
    <div class="age-badge"><span class="age-badge__label">Ages</span><span class="age-badge__range">6-18</span></div>

    <p class="footer-info">BOARD OF ED OT RSA'S ACCEPTED<br>Located in Maple Heights<br>Evaluations done in Maple Heights &amp; Cedar Grove<br>For more information or to be added to our email list,<br>please email: brightpathot@example.com</p>
    <div class="footer-rule"></div>
    <p class="contact">DANA LEVINSKY OTR/L<br>(555)014-2276</p>
  </article>
</body>
</html>
```